Eyecatching Design for Car price comparison website - read now! :)

We need a cool fresh responsive design for our website www.fahrzeug-preis-ermitteln.de ... it is a website where you can calculate the worth of your old used car for free.

We like the layout of http://www.gebrauchtwagenzentrale.de/ or https://www.qorm.de very much.

We want the customer to quickly understand how the website works and what he can do. The customer should develop trust to our calculation.

Our old Color green should be included.
Updates

Project Deadline Extended
Reason: Hey guys, some more designs are welcome... Now coded project! :)

Target Market(s)

People that want to sell their cars, men and women

Industry/Entity Type

Car Dealer

Coding

Coded - Design and coding required

Number of Pages Required

3 page

Font styles to use
Sans Serif

Colors
acd036

Requirements
Must have
• Attractive, Trusting, Responsive, Focus on functionality
Should not have
• To be to close to http://www.gebrauchtwagenzentrale.de/ or https://www.qorm.de

```html
<!DOCTYPE html>
<html lang="en">
<head>
<meta charset="utf-8">
<title>Fahrzeug Preis-Check Portal</title>
<link href="https://fonts.googleapis.com/css2?family=Ubuntu:wght@400;500;700&family=Lato:ital,wght@0,400;0,700;1,400&family=Poppins:wght@500;600&display=swap" rel="stylesheet">
<style>
:root{
  --green:#acd036;
  --green-dark:#97ba28;
  --ink:#222;
  --text:#444;
  --muted:#777;
  --line:#d9d9d9;
  --soft:#f4f5f7;
  --footer:#efefef;
  --white:#fff;
}
*{box-sizing:border-box;margin:0;padding:0}
html,body{width:1200px;height:2372px;overflow:hidden}
body{font-family:"Lato",sans-serif;color:var(--text);background:var(--white);position:relative}

/* header */
.site-header{height:90px;position:relative;background:linear-gradient(#fff,#f3f3f3)}
.brand{position:absolute;left:82px;top:16px}
.brand-name{font-family:"Ubuntu",sans-serif;font-weight:500;font-size:22px;color:var(--green)}
.brand-tag{font-size:15px;color:#333;margin-top:7px}
.contact{position:absolute;top:26px;display:flex;gap:10px;align-items:flex-start}
.contact-icon{width:34px;height:34px;border:2px solid var(--green);border-radius:4px;display:flex;align-items:center;justify-content:center}
.contact-label{font-size:13px;color:#555}
.contact-value{font-size:14px;color:#222;margin-top:3px}
.contact.phone{left:676px}
.contact.mail{left:880px}

/* nav */
.main-nav{height:43px;background:var(--green);position:relative}
.main-nav ul{list-style:none;display:flex;position:absolute;left:88px;top:0;height:43px}
.main-nav li{color:#fff;font-size:15px;height:43px;line-height:43px;padding:0 30px;position:relative}
.main-nav li+li::before{content:"";position:absolute;left:0;top:12px;height:20px;border-left:1px solid rgba(255,255,255,.45)}
.search{position:absolute;left:846px;top:5px;width:273px;height:34px;background:#fff;display:flex;align-items:center;justify-content:space-between;padding:0 12px}
.search span{font-size:12px;font-style:italic;color:#333}

/* hero */
.hero{height:580px;position:relative;background:linear-gradient(160deg,#f7c45a 0%,#e08a2a 25%,#8a5a2e 55%,#3b2a22 85%,#241a16 100%)}
.hero-arrow{position:absolute;top:272px}
.valuation-box{position:absolute;left:710px;top:103px;width:409px;height:381px;background:#fff;box-shadow:0 2px 10px rgba(0,0,0,.25)}
.valuation-title{height:45px;background:#f6f8ef;border-top:4px solid var(--green);padding:9px 22px 0;font-family:"Ubuntu",sans-serif;font-size:21px;color:var(--green)}
.valuation-body{padding:16px 22px 0;font-size:14px;color:#333}
.field{height:38px;border:1px solid #cfcfcf;font-size:12px;color:#444;display:flex;align-items:center;padding:0 10px;background:#fff}
.row{display:flex;align-items:center;gap:10px}
.info{width:22px;height:22px;border:2px solid var(--green);border-radius:50%;color:var(--green);font-size:13px;font-weight:700;display:flex;align-items:center;justify-content:center}
.btn{display:inline-flex;align-items:center;gap:8px;background:var(--green);color:#fff;font-weight:700;font-size:15px;height:30px;padding:0 12px}

/* how it works */
.how{height:452px;position:relative}
.section-title{font-family:"Ubuntu",sans-serif;font-weight:500;font-size:29px;color:var(--green);text-align:center}
.section-title::after{content:"";display:block;width:68px;height:2px;background:var(--green);margin:14px auto 0}
.how .section-title{position:absolute;top:52px;width:100%}
.step{position:absolute;top:147px;width:290px;text-align:center}
.step-circle{width:136px;height:136px;border-radius:50%;border:5px solid var(--green);background:radial-gradient(circle at 50% 40%,#555,#1e1e1e);margin:0 auto;display:flex;align-items:center;justify-content:center;box-shadow:0 12px 14px -8px rgba(0,0,0,.3)}
.step-name{font-family:"Ubuntu",sans-serif;font-size:25px;color:#222;margin-top:20px}
.step-text{font-size:14px;color:#333;line-height:18px;margin-top:12px;padding:0 22px}
.dots{position:absolute;top:206px;display:flex;align-items:center;gap:14px}
.dots i{display:block;border-radius:50%;background:#d5d5d5}

/* reviews */
.reviews{height:381px;position:relative;background:linear-gradient(180deg,#1b222c 0%,#2f3b4a 45%,#141a22 100%)}
.reviews .section-title{color:#fff;position:absolute;top:42px;width:100%}
.reviews .section-title::after{background:#fff;width:46px}
.review-card{position:absolute;top:130px;width:497px;height:172px;background:#fff;padding:8px;display:flex;gap:14px}
.review-photo{width:158px;height:156px;background:linear-gradient(160deg,#c9ced6,#7c8592)}
.review-body{flex:1;padding-top:2px}
.review-text{font-size:13px;font-style:italic;line-height:19px;color:#444}
.stars{display:flex;gap:3px;margin-top:10px}
.reviewer{font-family:"Poppins",sans-serif;font-weight:600;font-style:normal;font-size:14px;color:#111;margin-top:8px}
.slide-btn{position:absolute;top:264px;width:27px;height:27px;border:2px solid #fff;display:flex;align-items:center;justify-content:center}

/* car value */
.car-value{height:424px;position:relative}
.car-photo{position:absolute;left:81px;top:59px;width:324px;height:308px;background:linear-gradient(180deg,#e6e8c8 0%,#b9cf6a 45%,#8b9c7a 70%,#c8b89a 100%);border:6px solid #a9743d}
.car-photo::after{content:"";position:absolute;inset:16px;border:2px solid rgba(255,255,255,.8)}
.car-text{position:absolute;left:428px;top:70px;width:680px}
.car-text h2{font-family:"Ubuntu",sans-serif;font-weight:500;font-size:29px;color:var(--green)}
.car-text h2::after{content:"";display:block;width:68px;height:2px;background:var(--green);margin-top:10px}
.car-text p{font-size:12.3px;line-height:19px;color:#333;margin-top:14px}

/* newsletter */
.newsletter{height:267px;position:relative;background:var(--soft)}
.newsletter .section-title{position:absolute;top:34px;width:100%}
.newsletter-lead{position:absolute;left:303px;top:103px;font-size:16px;color:#222}
.subscribe{position:absolute;left:346px;top:190px;display:flex;height:42px}
.subscribe .email{width:400px;background:#fff;border:1px solid #ddd;font-size:12px;font-style:italic;color:#333;display:flex;align-items:center;padding:0 14px}
.subscribe .btn{height:42px;font-size:15px;padding:0 16px}

/* footer */
.footer-nav{height:90px;background:var(--footer);position:relative}
.footer-nav ul{list-style:none;display:flex;position:absolute;left:82px;top:36px}
.footer-nav li{font-size:18px;color:#222;margin-right:58px;letter-spacing:.3px}
.social{position:absolute;left:913px;top:28px;display:flex;gap:12px}
.social i{display:block;width:32px;height:32px;border-radius:50%;background:#3a4250}
.copyright{height:45px;background:var(--green);color:#fff;font-size:13px;text-align:center;line-height:45px}
</style>
</head>
<body>

<header class="site-header">
  <div class="brand">
    <div class="brand-name">Fahrzeug Preis-Check Portal (beta)</div>
    <div class="brand-tag">Free &amp; Used Car Price check without registration</div>
  </div>
  <div class="contact phone">
    <div class="contact-icon"><svg width="18" height="18" viewBox="0 0 24 24"><path d="M6.6 10.8a15 15 0 0 0 6.6 6.6l2.2-2.2a1 1 0 0 1 1-.25 11.4 11.4 0 0 0 3.6.57 1 1 0 0 1 1 1V20a1 1 0 0 1-1 1A17 17 0 0 1 3 4a1 1 0 0 1 1-1h3.5a1 1 0 0 1 1 1c0 1.25.2 2.45.57 3.57a1 1 0 0 1-.25 1z" fill="#acd036"/></svg></div>
    <div><div class="contact-label">Call Us</div><div class="contact-value">+49 (0) 3012 555 0199</div></div>
  </div>
  <div class="contact mail">
    <div class="contact-icon"><svg width="20" height="16" viewBox="0 0 20 16"><rect x="1" y="1" width="18" height="14" fill="#acd036"/><path d="M1 1l9 7 9-7" stroke="#fff" stroke-width="1.6" fill="none"/></svg></div>
    <div><div class="contact-label">Email Us</div><div class="contact-value">kontakt [at] preiswert-mail . de</div></div>
  </div>
</header>

<nav class="main-nav">
  <ul>
    <li>Learn</li><li>Auto Number</li><li>Car List</li><li>Imprint</li><li>Tweet</li>
  </ul>
  <div class="search"><span>Search here</span>
    <svg width="18" height="18" viewBox="0 0 20 20"><circle cx="8" cy="8" r="6" stroke="#111" stroke-width="2.6" fill="none"/><path d="M12.5 12.5L18 18" stroke="#111" stroke-width="3" stroke-linecap="round"/></svg>
  </div>
</nav>

<section class="hero" role="img" aria-label="Photo of two people in a convertible driving down a sunlit country road">
  <svg class="hero-arrow" style="left:22px" width="16" height="30" viewBox="0 0 16 30"><path d="M14 2L2 15l12 13" stroke="#fff" stroke-width="2.5" fill="none"/></svg>
  <svg class="hero-arrow" style="right:22px" width="16" height="30" viewBox="0 0 16 30"><path d="M2 2l12 13L2 28" stroke="#fff" stroke-width="2.5" fill="none"/></svg>
  <form class="valuation-box">
    <div class="valuation-title">Which car value is to be evaluated?</div>
    <div class="valuation-body">
      <div>Insert offer URL to a comparable car here</div>
      <div class="row" style="margin-top:12px">
        <div class="field" style="width:336px">http://www.fahrzeugmarkt-beispiel.de/angebot?id=xyz</div>
        <div class="info">i</div>
      </div>
      <div style="margin-top:20px">Enter OR Vehicle key</div>
      <div class="row" style="margin-top:12px">
        <span>HSN:</span><div class="field" style="width:114px">000</div>
        <span style="margin-left:8px">TSN:</span><div class="field" style="width:114px">000</div>
        <div class="info">i</div>
      </div>
      <div style="margin-top:20px">Select OR Car Brand</div>
      <div class="row" style="margin-top:12px">
        <span>Brand:</span>
        <div class="field" style="width:152px;justify-content:space-between">Select Brand
          <svg width="12" height="8" viewBox="0 0 12 8"><path d="M1 1l5 5 5-5" stroke="#222" stroke-width="2" fill="none"/></svg></div>
      </div>
      <div class="btn" style="margin-top:28px">Submit <svg width="7" height="11" viewBox="0 0 7 11"><path d="M1 1l4.5 4.5L1 10" stroke="#fff" stroke-width="2" fill="none"/></svg></div>
    </div>
  </form>
</section>

<section class="how">
  <h2 class="section-title">How It Works</h2>
  <div class="step" style="left:87px">
    <div class="step-circle"><svg width="70" height="70" viewBox="0 0 70 70"><circle cx="29" cy="29" r="19" stroke="#fff" stroke-width="5" fill="none"/><circle cx="29" cy="24" r="6" fill="#fff"/><path d="M18 38a11 9 0 0 1 22 0z" fill="#fff"/><path d="M43 43l16 16" stroke="#fff" stroke-width="8" stroke-linecap="round"/></svg></div>
    <div class="step-name">Opinion</div>
    <div class="step-text">Lorem ipsum dolor sit amet consectetuer adipiscing elit, sed diam nonummy nibh.</div>
  </div>
  <div class="dots" style="left:356px"><i style="width:8px;height:8px"></i><i style="width:12px;height:12px"></i><i style="width:17px;height:17px"></i><i style="width:24px;height:24px"></i></div>
  <div class="step" style="left:451px">
    <div class="step-circle"><svg width="70" height="70" viewBox="0 0 70 70"><rect x="26" y="8" width="30" height="22" rx="2" transform="rotate(20 41 19)" fill="#fff"/><circle cx="41" cy="19" r="5" fill="#2a2a2a"/><rect x="12" y="32" width="10" height="28" rx="2" fill="#fff"/><path d="M25 34h22a5 5 0 0 1 0 10h-4a5 5 0 0 1 0 8h-4a4 4 0 0 1 0 8H25z" fill="#fff"/></svg></div>
    <div class="step-name">Payment</div>
    <div class="step-text">Lorem ipsum dolor sit amet consectetuer adipiscing elit, sed diam nonummy nibh.</div>
  </div>
  <div class="dots" style="left:720px"><i style="width:8px;height:8px"></i><i style="width:12px;height:12px"></i><i style="width:17px;height:17px"></i><i style="width:24px;height:24px"></i></div>
  <div class="step" style="left:815px">
    <div class="step-circle"><svg width="70" height="70" viewBox="0 0 70 70"><path d="M20 50L44 14l8 6-24 36-10 4z" fill="#fff"/><path d="M12 60h46" stroke="#fff" stroke-width="5" stroke-linecap="round"/><path d="M14 12l44 44" stroke="#2a2a2a" stroke-width="9"/><path d="M14 12l44 44" stroke="#fff" stroke-width="4" stroke-linecap="round"/></svg></div>
    <div class="step-name">Signing Off</div>
    <div class="step-text">Lorem ipsum dolor sit amet consectetuer adipiscing elit, sed diam nonummy nibh.</div>
  </div>
</section>

<section class="reviews" role="img" aria-label="Dark photo of a car in an underground garage">
  <h2 class="section-title">Customer Reviews</h2>
  <div class="slide-btn" style="left:34px"><svg width="14" height="10" viewBox="0 0 14 10"><path d="M13 5H2M5 1L1 5l4 4" stroke="#fff" stroke-width="1.8" fill="none"/></svg></div>
  <div class="slide-btn" style="right:34px"><svg width="14" height="10" viewBox="0 0 14 10"><path d="M1 5h11M9 1l4 4-4 4" stroke="#fff" stroke-width="1.8" fill="none"/></svg></div>
  <article class="review-card" style="left:90px">
    <div class="review-photo" role="img" aria-label="Portrait photo of the customer"></div>
    <div class="review-body">
      <div class="review-text">Lorem ipsum dolor sit amet, consectetuerie adipiscing elit, sed diam nonummy nibhtatin euismod tincidunt ut laoreet dolore magnai aliquam erat volutpatut wisi enim ad minim veniam quis nostrud exerci tation.</div>
      <div class="stars">
        <svg width="86" height="14" viewBox="0 0 86 14"><g fill="#acd036"><path id="star" d="M7 0l2 5h5l-4 3 2 5-5-3-5 3 2-5-4-3h5z"/><use href="#star" x="18"/><use href="#star" x="36"/><use href="#star" x="54"/><use href="#star" x="72"/></g></svg>
      </div>
      <div class="reviewer">Mara Lenz</div>
    </div>
  </article>
  <article class="review-card" style="left:615px">
    <div class="review-photo" role="img" aria-label="Portrait photo of the customer" style="background:linear-gradient(160deg,#8a5a44,#c24a4a)"></div>
    <div class="review-body">
      <div class="review-text">Lorem ipsum dolor sit amet, consectetuerie adipiscing elit, sed diam nonummy nibhtatin euismod tincidunt ut laoreet dolore magnai aliquam erat volutpatut wisi enim ad minim veniam quis nostrud exerci tation.</div>
      <div class="stars">
        <svg width="86" height="14" viewBox="0 0 86 14"><g fill="#acd036"><use href="#star"/><use href="#star" x="18"/><use href="#star" x="36"/><use href="#star" x="54"/></g><use href="#star" x="72" fill="#cfcfcf"/></svg>
      </div>
      <div class="reviewer">Jonas Feld</div>
    </div>
  </article>
</section>

<section class="car-value">
  <div class="car-photo" role="img" aria-label="Photo of a blue compact car framed by an open gateway with trees behind"></div>
  <div class="car-text">
    <h2>The Car Value</h2>
    <p>Anyone a Used Car Buy or his old sell car will not come around it to make a realistic idea about the price. Often an objective is evaluating a used car costs. But there is also free car value calculator or auto-lists may provide that the same benefits as a premium offerings. And of course with significantly fewer circumstances and time.</p>
    <p>On this page you can in different ways the value of his car determine. Each of them is almost self-explanatory. If you have a car on the usual car sales focus -Internetportalen eye, you can simply enter the checkmark to confirm the offer URL on the edge - and you come to a detailed overview. Here it is shown which features were included in the evaluation and how much is the value of the car.</p>
    <p>If the code numbers are available can be of value also simply determine it. Just as easily select from a list to be evaluated car. It can from the top be and all this without register to have. If you use the review by URL is an equally displayed, whether the price of the desired car is above or below the calculated value, thus facilitating the purchase decision. Furthermore, there is a feeling of how far one can still negotiate with the seller. When his car in car sales Internet portals to sell, a free car review is a good indication how much money you can potentially get even.</p>
  </div>
</section>

<section class="newsletter">
  <h2 class="section-title">Newsletter Sign Up</h2>
  <div class="newsletter-lead">Lorem ipsum dolor sit amet, consectetuer adipiscing elit, sed diam nonummy nibh e.</div>
  <svg style="position:absolute;left:250px;top:120px" width="110" height="95" viewBox="0 0 110 95"><path d="M2 20L70 2 32 30z" fill="#555"/><path d="M32 30l38-28-26 36z" fill="#888"/><path d="M32 30l2 16 10-8" fill="#444"/><path d="M36 44c-10 14 -4 30 20 34s36 8 44 14" stroke="#555" stroke-width="1.5" stroke-dasharray="3 4" fill="none"/></svg>
  <div class="subscribe">
    <div class="email">Enter your email address</div>
    <div class="btn">SUBSCRIBE <svg width="7" height="11" viewBox="0 0 7 11"><path d="M1 1l4.5 4.5L1 10" stroke="#fff" stroke-width="2" fill="none"/></svg></div>
  </div>
</section>

<footer>
  <div class="footer-nav">
    <ul><li>LEARN</li><li>AUTO NUMBER</li><li>CAR LIST</li><li>IMPRINT</li><li>TWEET</li></ul>
    <div class="social" aria-label="Social links"><i></i><i></i><i></i><i></i><i></i></div>
  </div>
  <div class="copyright">Copyright © 2016 FAHRZEUG-PREIS-ERMITTELN.DE &nbsp;|&nbsp; All Rights Reserved.</div>
</footer>

</body>
</html>
```